Private School Website Revamp

We need a new design for the private school's website revamp. The new website will be using WordPress CMS, but we will be using it to handle custom data types, not blogs - so the content will not be typical blog-style.

The school has indicated the following template which they like, and our design to follow the design style.
http://qrv7.layoutkiosk-demo.com/sitekit_48215/
However, follow the school's colour-theme and sitemap.

Colour-theme: White, Green (refer to current website - www.morvelan.com.sg)

Sitemap: (for navigation menu)
- Home
- Academic & Examination Board
- Our Philosophy
- Our Programmes
+ Preparatory Courses
+ Tuition Classes
+ Study Tours
- Our Hostel
- Trial Tests
+ English
+ Mathematics
- Contact Us

Target Market(s)

Parents looking for private school services.
Existing students of the private school accessing trial tests.

Industry/Entity Type

School

Requirements
Must have
• Homepage design to include
• - Logo, navigation menu, search box
• - Featured area/slideshow (see prefered template above)
• - Section for Preparatory Courses
• - Section for Tuition Classes
• - Section for Study Tours
• - Section for Hostel Stay
• - Awards & Certification box
• - Footer contact details
Nice to have
• - Pictures of happy students
• - The Message from Director box is "nice to have", but no necessary if it does not fit into homepage design.

```html
<!DOCTYPE html>
<html lang="en">
<head>
<meta charset="utf-8">
<title>Morvelan Private School</title>
<link rel="stylesheet" href="https://fonts.googleapis.com/css2?family=Gelasio&family=Ubuntu:wght@400;500;700&display=swap">
<style>
:root{
  --green:#33a014;
  --green-dark:#1d5e0b;
  --green-text:#3a7a06;
  --yellow:#ffc20e;
  --sky-top:#8fb6df;
  --sky-bottom:#eef3f9;
  --panel-border:#e1e6ea;
  --text:#222;
  --white:#fff;
  --footer-top:#8cc844;
  --footer-bottom:#3f8c14;
}
*{box-sizing:border-box;margin:0;padding:0}
html,body{width:928px;height:1200px;overflow:hidden;background:var(--white)}
body{position:relative;font-family:"Ubuntu",sans-serif;color:var(--text)}
.abs{position:absolute}
.hero{left:0;top:0;width:928px;height:301px;background:linear-gradient(180deg,var(--sky-top),#c9daee 55%,var(--sky-bottom))}
.hero-photo{left:320px;top:8px;width:380px;height:293px;border-radius:40px 40px 0 0;background:linear-gradient(180deg,#6f8fb4,#9aa9b8 60%,#b4bcc4)}
.brand{left:19px;top:14px;display:flex;align-items:center;gap:10px}
.brand-mark{width:46px;height:46px;background:var(--green-dark);border-radius:6px}
.brand-name{font-weight:700;font-size:19px;color:var(--green-dark);letter-spacing:.5px}
.langs{right:44px;top:27px;font-size:10.5px;color:#222}
.langs span{margin:0 4px}
.nav{left:19px;top:301px;width:890px;height:46px;background:var(--yellow);border-radius:8px 8px 0 0;display:flex;align-items:center;font-size:13.5px;overflow:hidden}
.nav a{color:#222;text-decoration:none;padding:0 17px}
.nav a.current{background:var(--green-dark);color:var(--white);height:100%;display:flex;align-items:center;padding:0 26px 0 29px;margin-right:2px}
.feature{top:356px;width:215px;height:190px;border:1px solid var(--panel-border);border-radius:10px;background:linear-gradient(180deg,#fff,#f5f7f8)}
.feature .pill{position:absolute;left:12px;top:14px;width:196px;height:39px;border-radius:6px;background:linear-gradient(180deg,#8fd14a,#3f9a16);font-family:"Gelasio",serif;color:var(--white);font-size:17px;line-height:16px;display:flex;align-items:center;padding-left:66px}
.feature .icon{position:absolute;left:6px;top:8px;width:48px;height:50px;border-radius:12px;background:linear-gradient(180deg,#b9cfe4,#4d7fb1)}
.feature .rule{position:absolute;left:16px;right:16px;top:70px;border-top:1px dotted #ccc}
.feature h4{position:absolute;left:17px;top:82px;font-size:11px;color:var(--green-text);font-weight:700}
.feature p{position:absolute;left:16px;top:105px;width:185px;font-size:11.5px;line-height:16px;color:#333}
.read-more{position:absolute;left:15px;top:150px;display:flex;align-items:center;gap:7px;font-size:11.5px;font-weight:700;color:#222}
.dot{width:22px;height:22px;border-radius:50%;background:radial-gradient(circle at 40% 35%,#b8e67a,#4fa51a);display:flex;align-items:center;justify-content:center}
.bar{height:30px;background:var(--green);border-radius:14px 14px 0 0;font-family:"Gelasio",serif;color:#fff;font-size:19px;line-height:30px}
.panel{border:1px solid var(--panel-border);border-top:none;border-radius:0 0 10px 10px;background:linear-gradient(180deg,#fff,#f7f8f9)}
.sec-title{font-size:18.5px;color:var(--green-dark);font-weight:400}
.body-text{font-size:10.5px;line-height:15.7px;color:#222}
.byline{font-size:10.5px;font-weight:700;margin-top:6px}
.dotted{border-top:1px dotted #ccc}
.btn{left:674px;top:738px;width:220px;height:40px;border-radius:4px;background:linear-gradient(180deg,#4fb21d,#1f6a0a);color:#fff;font-size:13.5px;display:flex;align-items:center;justify-content:center}
.badge{left:669px;width:220px}
.caption{left:669px;width:220px;text-align:center;font-size:13px}
.footer{left:18px;top:1029px;width:892px;height:163px;border-radius:12px;background:linear-gradient(180deg,var(--footer-top),var(--footer-bottom))}
.footer .addr{position:absolute;left:19px;top:14px;color:#fff;font-size:10.5px;line-height:16.7px}
.footer .addr strong{display:block;font-weight:400;font-size:13px;color:#0f3f05;margin-bottom:2px}
.footer .fbrand{position:absolute;right:20px;top:70px;display:flex;align-items:center;gap:10px}
.footer .fbrand .brand-mark{background:#173d08;width:40px;height:40px}
.footer .fbrand .brand-name{color:#fff;font-size:18px}
.footer .copy{position:absolute;right:20px;top:128px;color:#fff;font-size:10.5px}
</style>
</head>
<body>

<header>
  <div class="abs hero" role="img" aria-label="Bright cloudy sky backdrop"></div>
  <div class="abs hero-photo" role="img" aria-label="Photo of four happy students running toward the camera carrying books"></div>
  <div class="abs brand"><div class="brand-mark"></div><div class="brand-name">MORVELAN PRIVATE SCHOOL</div></div>
  <div class="abs langs">English<span>|</span>Bahasa indonesia<span>|</span>Other</div>
  <nav class="abs nav">
    <a class="current">Home</a>
    <a>Academic &amp; Examination Board</a>
    <a>Our Philosophy</a>
    <a>Our Programmes</a>
    <a>Our Hostel</a>
    <a>Trial Tests</a>
    <a>Contact Us</a>
  </nav>
</header>

<main>
  <section class="abs feature" style="left:17px">
    <div class="pill">Tuition Classes</div>
    <div class="icon" role="img" aria-label="Book icon"></div>
    <div class="rule"></div>
    <h4>Lorem ipsum dolor sit amet</h4>
    <p>Cum sociis natoque penatibus et magnis dis parturient ontes.</p>
    <div class="read-more"><span class="dot"><svg width="10" height="10" viewBox="0 0 10 10"><path d="M2 2l3 3-3 3M5 2l3 3-3 3" stroke="#fff" stroke-width="1.4" fill="none"/></svg></span>Read More</div>
  </section>
  <section class="abs feature" style="left:243px">
    <div class="pill">Preparatory<br>Courses</div>
    <div class="icon" role="img" aria-label="Clock icon" style="border-radius:50%"></div>
    <div class="rule"></div>
    <h4>Lorem ipsum dolor sit amet</h4>
    <p>Nuno valencia esta de demaria andn uno di cartia margarute</p>
    <div class="read-more"><span class="dot"><svg width="10" height="10" viewBox="0 0 10 10"><path d="M2 2l3 3-3 3M5 2l3 3-3 3" stroke="#fff" stroke-width="1.4" fill="none"/></svg></span>Read More</div>
  </section>
  <section class="abs feature" style="left:469px">
    <div class="pill">Study Tours</div>
    <div class="icon" role="img" aria-label="Globe with information sign icon" style="border-radius:50%;background:linear-gradient(180deg,#8fd14a,#2f6fae)"></div>
    <div class="rule"></div>
    <h4>Lorem ipsum dolor sit amet</h4>
    <p>Phasellus id lobortis eros. Cras vitae risus mauris. Nulla non.</p>
    <div class="read-more"><span class="dot"><svg width="10" height="10" viewBox="0 0 10 10"><path d="M2 2l3 3-3 3M5 2l3 3-3 3" stroke="#fff" stroke-width="1.4" fill="none"/></svg></span>Read More</div>
  </section>
  <section class="abs feature" style="left:695px">
    <div class="pill">Our Hostel</div>
    <div class="icon" role="img" aria-label="House icon" style="background:linear-gradient(180deg,#5f94d2,#e8eef4)"></div>
    <div class="rule"></div>
    <h4>Lorem ipsum dolor sit amet</h4>
    <p>Vestibulum augue lacus, suscipit quis convallis commodo, mollis.</p>
    <div class="read-more"><span class="dot"><svg width="10" height="10" viewBox="0 0 10 10"><path d="M2 2l3 3-3 3M5 2l3 3-3 3" stroke="#fff" stroke-width="1.4" fill="none"/></svg></span>Read More</div>
  </section>

  <div class="abs bar" style="left:19px;top:558px;width:602px;padding-left:24px">About Us</div>
  <section class="abs panel" style="left:29px;top:588px;width:582px;height:171px;padding:16px 14px 0 13px">
    <h2 class="sec-title">WELCOME TO MORVELAN PRIVATE SCHOOL</h2>
    <p class="body-text" style="margin-top:6px">Lorem ipsum dolor sit amet, consectetur adipiscing elit. Cras neque erat, aliquet eget gravida sit amet, viverra non erat. Donec libero turpis, gravida et congue a, rhoncus at lacus. Integer in justo ut tortor scelerisque fermentum ac porttitor magna. Proin condimentum nibh vitae metus placerat ut egestas mauris iaculis. Suspendisse potenti. Maecenas ultrices, arcu et condimentum molestie, ligula turpis condimentum ligula, et cursus eros nibh eu felis. Nam dui ante, aliquam eget viverra et, congue quis augue. Aenean convallis dictum lectus ac aliquet. Sed varius urna sed arcu consectetur tincidunt. Curabitur vel mi quis libero aliquam egestas non sit amet leo.</p>
  </section>

  <div class="abs bar" style="left:19px;top:772px;width:602px;padding-left:24px">Testimonials</div>
  <section class="abs panel" style="left:29px;top:802px;width:582px;height:214px;padding:16px 16px 0 12px">
    <h2 class="sec-title">PARENTS TESTIMONIAL</h2>
    <p class="body-text" style="margin-top:6px">Etiam at risus purus, ac lacinia lacus. Duis at ante ante, nec varius felis. Cras massa ligula, feugiat sit amet tempor eget, euismod sagittis odio. Nullam rhoncus urna molestie dui euismod gravida.</p>
    <p class="byline">By Abcd Parents</p>
    <div class="dotted" style="margin:10px 0 6px"></div>
    <p class="body-text">Etiam at risus purus, ac lacinia lacus. Duis at ante ante, nec varius felis. Cras massa ligula, feugiat sit amet tempor eget, euismod sagittis odio. Nullam rhoncus urna molestie dui euismod gravida.</p>
    <p class="byline">By Abcd Parents</p>
    <div class="dotted" style="margin:12px 0 8px"></div>
    <p style="text-align:right;font-size:10.5px;font-weight:700;display:flex;justify-content:flex-end;align-items:center;gap:5px"><svg width="12" height="12" viewBox="0 0 12 12"><rect width="12" height="12" rx="3" fill="#3f9a16"/><path d="M5 3l3 3-3 3" stroke="#fff" stroke-width="1.5" fill="none"/></svg>Read More Testimonials</p>
  </section>

  <div class="abs bar" style="left:643px;top:558px;width:267px;text-align:center">Announcements</div>
  <section class="abs panel" style="left:661px;top:588px;width:241px;height:201px;padding:14px 0 0 18px">
    <h3 style="font-weight:400;font-size:15.5px">CAREER OPPORTUNITIES</h3>
    <p style="font-size:10.5px;font-weight:700;margin:2px 0 0 3px">13 FEBRUARY, 2010</p>
    <ul style="list-style:none;font-size:10px;line-height:15px;margin:12px 0 0 6px">
      <li style="display:flex;gap:6px"><span style="color:var(--green)">::</span><span style="text-decoration:underline">Primary / Secondary Chinese Teacher<br>(Part time)</span></li>
      <li style="display:flex;gap:6px;margin-top:7px"><span style="color:var(--green)">::</span><span style="text-decoration:underline">Centre Manager, School Administrators<br>(Full / Part Time).</span></li>
    </ul>
  </section>
  <div class="abs btn">Read More Announcements</div>

  <div class="abs bar" style="left:643px;top:801px;width:267px;text-align:center">Awards &amp; Certificates</div>
  <section class="abs panel" style="left:655px;top:831px;width:248px;height:185px"></section>
  <div class="abs badge" style="top:844px;height:55px;background:#1a3e95" role="img" aria-label="Accreditation badge"></div>
  <div class="abs caption" style="top:904px">Morvelan Private School</div>
  <div class="abs badge" style="top:926px;height:56px;background:#0e3a0b" role="img" aria-label="Education award badge"></div>
  <div class="abs caption" style="top:989px">Morvelan Student Hostel</div>
</main>

<footer class="abs footer">
  <div class="addr">
    <strong>Address</strong>
    48 Larkspur Rise Ave 3<br>
    Fernhill Civic Centre, # 02 -07<br>
    S(604417)<br>
    Telephone No. +65 6100 2481<br>
    Fax: +65 6100 2482<br>
    Email: school@morvelan.com.sg
  </div>
  <div class="fbrand"><div class="brand-mark"></div><div class="brand-name">MORVELAN PRIVATE SCHOOL</div></div>
  <div class="copy">© 2010, Morvelan Private School &nbsp;|&nbsp; All Rights Reserved</div>
</footer>

</body>
</html>
```